Business card for Sports Apparel business

DOUBLE SIDED DESIGN
We need business cards for a new sports apparel business. We are developing a protective headband for soccer initially.
Corvell is focused on designing and developing head protection products to reduce the likelihood of concussion when playing sports. Exploring and understanding medical insights, material science research, current and former players experiences and governing bodies guidelines has allowed Corvell to develop the safety, style, form and function requirements of a suitable product to bring to market.
Target Market(s)
Mums buying kits for the sons and daughters. Amateur footballers.
Industry/Entity Type
Sporting Good
Contact Information for Business Card
Martin Ashgrove - CEO
Mobile: +44 7391608254
Email: martin@corvell.co.uk
Tel: 0208 5143927
Helena Pardoe - COO
Mob: +44 7356 409183
Email: helena@corvell.co.uk
Tel: 0208 5143927
Duncan Wyvern - CCO
Mob: +44 7468 230517
Email: duncan@corvell.co.uk
Tel: 0208 5143927
Look and feel

```html
<!DOCTYPE html>
<html lang="en">
<head>
<meta charset="utf-8">
<title>Corvell business card</title>
<link rel="stylesheet" href="https://fonts.googleapis.com/css2?family=Open+Sans:wght@400;700&family=Montserrat:wght@400&display=swap">
<style>
  :root {
    --brand-blue: #135f95;
    --card-white: #ffffff;
    --text-grey: #5a5a5a;
    --backdrop: #3a3634;
  }
  * { margin: 0; padding: 0; box-sizing: border-box; }
  html, body {
    width: 1200px; height: 716px; overflow: hidden;
    background: var(--backdrop);
  }
  .sheet {
    position: relative; width: 1200px; height: 716px;
    display: flex; align-items: center; justify-content: center; gap: 40px;
  }
  .card {
    width: 540px; height: 309px; position: relative;
    box-shadow: 0 10px 28px rgba(0,0,0,0.45);
  }
  .card-front {
    background: var(--brand-blue);
    display: flex; align-items: center; justify-content: center;
  }
  .wordmark {
    display: flex; align-items: center; gap: 14px;
    color: var(--card-white);
    font-family: "Open Sans", sans-serif; font-weight: 700;
    font-size: 54px; letter-spacing: 2px; text-transform: uppercase;
  }
  .wordmark-square {
    width: 22px; height: 22px; background: var(--card-white);
  }
  .card-back { background: var(--card-white); }
  .identity {
    position: absolute; right: 236px; top: 120px; text-align: right;
  }
  .person-name {
    font-family: "Open Sans", sans-serif; font-weight: 700;
    font-size: 19px; color: var(--brand-blue); letter-spacing: 0.6px;
  }
  .person-role {
    font-family: "Montserrat", sans-serif; font-size: 11px;
    color: var(--text-grey); margin-top: 4px;
  }
  .divider {
    position: absolute; left: 318px; top: 138px;
    width: 1.5px; height: 52px; background: var(--brand-blue);
  }
  .contacts {
    position: absolute; left: 334px; top: 136px; list-style: none;
    font-family: "Montserrat", sans-serif; font-size: 11.5px;
    color: var(--text-grey); line-height: 15px;
  }
  .contacts li { display: flex; align-items: center; gap: 5px; }
  .contacts svg { width: 9px; height: 9px; fill: var(--brand-blue); flex: none; }
</style>
</head>
<body>
<main class="sheet">
  <section class="card card-front" aria-label="Card front">
    <div class="wordmark"><span class="wordmark-square"></span>Corvell</div>
  </section>

  <section class="card card-back" aria-label="Card back">
    <div class="identity">
      <p class="person-name">Martin Ashgrove</p>
      <p class="person-role">CEO</p>
    </div>
    <div class="divider"></div>
    <ul class="contacts">
      <li>
        <svg viewBox="0 0 10 10"><path d="M2 0.5 L3.8 2.6 L2.9 3.6 Q4 6 6.4 7.1 L7.4 6.2 L9.5 8 L8.2 9.5 Q1.5 8.5 0.5 1.8 Z"/></svg>
        0208 5143927
      </li>
      <li>
        <svg viewBox="0 0 10 10"><path d="M2.5 0 H7.5 V10 H2.5 Z M3.3 1 V8.2 H6.7 V1 Z"/></svg>
        +44 7391608254
      </li>
      <li>
        <svg viewBox="0 0 10 10"><path d="M0 2 H10 V8.5 H0 Z M0.8 2.6 L5 5.6 L9.2 2.6 Z" fill-rule="evenodd"/></svg>
        martin@corvell.co.uk
      </li>
      <li>
        <svg viewBox="0 0 10 10"><circle cx="5" cy="5" r="4.6"/><path d="M0.5 5 H9.5 M5 0.5 V9.5" stroke="#fff" stroke-width="0.7"/></svg>
        www.corvell.co.uk
      </li>
    </ul>
  </section>
</main>
</body>
</html>
```